Website Design for NYC Female Attorney – Clean, Warm, Professional

Maren Holbeck, Esq.
www.MarenTHolbeckLegal.example

I’m a New York City-based attorney and CPA with a reputation for providing thoughtful, high-integrity legal guidance in both estate planning and small business law. I’ve served over 500 clients, and maintain a perfect 5-star rating. Clients come to me for clarity, compassion, and results — and I want my new website to reflect that.

**🎯 WHAT I NEED:**
A clean, modern, and emotionally resonant website that highlights who I am, what I do, and why clients trust me. It must feel approachable and warm, but still professional and elegant — think Quorvex meets boutique law firm. Feminine but not frilly.

**🧩 CORE WEBSITE SECTIONS (Top Navigation):**

1. **Home** – Strong first impression, tagline, CTA (book a call)
Homepage Copy (Sample Layout)
Headline:
Trusted Legal Guidance for Families and Founders.

Subheading:
Whether you’re protecting what you’ve built or building what’s next, I help you navigate estate planning and business law with confidence, compassion, and clarity.

Tagline (beneath logo or footer):
Legal Clarity for Life and Business.
2. **About Maren** – Bio, personal approach, credentials
3. **Services**

* *Estate Planning*
* *Business Law*
4. **Who I Work With** – Ideal clients (parents, entrepreneurs, etc.)
5. **Testimonials** – Client praise and social proof
6. **Success Stories** – Highlighting wins and case types
7. **FAQs** – Warm and clear answers to common questions
8. **Blog** – Thought leadership and helpful tips
8.5 Events
9. **Contact / Book a Call** – Scheduling or contact form

**🖼 STYLE DIRECTION:**

* Clean white backgrounds, soft jewel tones or neutrals
* Professional headshots and personal branding assets available
* Emphasis on readability, trust, and ease of navigation - THIS NEEDS TO BE BUILT OUT SO IT IS TRUSTED BY AI!
* No harsh colors, no corporate/legal clichés (e.g., gavels or scales) - I MEAN THIS. I DO NOT WANT A BORING LAW WEBSITE WITH SCALES AND GAVELS
* Feminine edge (not pink-heavy), with strong hierarchy and callouts

**💡 DESIGN NOTES:**

* Mobile-first design required
* Should include space for video or welcome message
* Easy to update blog or CMS area preferred
* Built in a user-friendly platform like WordPress, Webflow, or similar
* Needs to feel elevated enough to support high-end flat fee packages

**📣 TONE:**
Smart. Warm. Sophisticated. Human.

**⚖️ FINAL DELIVERABLES:**

* Homepage + 5+ interior pages
* Desktop + mobile views
* Style guide (fonts, colors, buttons)
* Bonus if you can help with copy layout/structure (not just visuals)

**📍TARGET AUDIENCE:**

* Busy professionals and families in NYC
* Women and couples who want peace of mind
* Entrepreneurs and creatives needing solid legal support

Here is my current site: www.MarenTHolbeckLegal.example
And here is a second business I have: www.QuickDayCounselDesk.example

Target Market(s)

Families and business owners

Industry/Entity Type

Law

Number of Pages Required

5+ page

Font styles to use
Serif
Sans Serif
Script

Requirements
Must have
• This website must be built to be seen as trustworthy by AI.

```html
<!DOCTYPE html>
<html lang="en">
<head>
<meta charset="utf-8">
<title>Maren Holbeck, Esq. – Estate Planning &amp; Business Law</title>
<link rel="stylesheet" href="https://fonts.googleapis.com/css2?family=Outfit:wght@400;500;600&family=Montserrat:wght@400;500;600&family=Cormorant+Garamond:wght@500&display=swap">
<style>
:root{
  --pink:#ff4f97;
  --navy:#2f3552;
  --ink:#1f2233;
  --muted:#7a7d8c;
  --card:#ffffff;
  --soft:#f2f2f5;
  --numeral:#e6e6ea;
  --white:#ffffff;
}
*{box-sizing:border-box;margin:0;padding:0}
html,body{width:1200px;height:4505px;overflow:hidden}
body{position:relative;background:var(--white);font-family:"Montserrat",sans-serif;color:var(--ink)}
.abs{position:absolute}
.h2{position:absolute;font-family:"Outfit",sans-serif;font-weight:500;font-size:38px;letter-spacing:-1.2px;color:var(--ink);text-align:center;width:1200px;left:0}
.btn{position:absolute;display:flex;align-items:center;justify-content:space-between;background:var(--pink);color:var(--white);border-radius:30px;font-size:14px;font-weight:500;padding:0 6px 0 26px;box-shadow:0 4px 10px rgba(255,79,151,.25);white-space:nowrap}
.btn .arrow{width:38px;height:38px;border-radius:50%;background:var(--white);display:flex;align-items:center;justify-content:center;flex:none}
.btn.light{background:var(--white);color:var(--ink)}
.btn.light .arrow{background:var(--navy)}
.photo{position:absolute;border-radius:14px}

/* hero */
.hero{position:absolute;left:0;top:0;width:1200px;height:749px;background:linear-gradient(100deg,#3e4660 0%,#55607a 45%,#7c8496 70%,#9aa0ad 100%)}
.hero .shade{position:absolute;inset:0;background:linear-gradient(90deg,rgba(40,46,70,.75),rgba(40,46,70,.15))}
.topbar{position:absolute;left:89px;top:17px;width:1022px;height:88px;background:rgba(60,66,88,.78);border-radius:10px;display:flex;align-items:center;padding:0 14px 0 16px}
.brand{font-family:"Cormorant Garamond",serif;font-weight:500;color:var(--white);font-size:19px;letter-spacing:1.5px;white-space:nowrap;display:flex;align-items:center;gap:8px}
.brand .dot{width:11px;height:11px;border:1.5px solid var(--white);border-radius:50%;flex:none}
.nav{display:flex;gap:20px;margin-left:44px;font-size:14px;color:var(--white);letter-spacing:-.3px;white-space:nowrap}
.search{margin-left:auto;width:40px;height:40px;border-radius:50%;background:var(--white);display:flex;align-items:center;justify-content:center}
.topbar .btn{position:static;margin-left:14px;height:48px;width:164px}
.hero-title{position:absolute;left:89px;top:200px;font-family:"Outfit",sans-serif;font-weight:500;font-size:82px;line-height:88px;letter-spacing:-3px;color:var(--white)}
.hero-title small{font-size:24px;letter-spacing:-.8px;margin-left:12px}
.hero-lead{position:absolute;left:89px;top:468px;width:540px;font-size:13.5px;line-height:22px;color:var(--white)}
.explore{position:absolute;left:889px;top:481px;width:122px;height:122px;border-radius:50%;background:rgba(255,255,255,.18);border:1px solid rgba(255,255,255,.55)}

/* services */
.svc{position:absolute;top:906px;width:372px;height:199px;background:var(--card);border-radius:14px;box-shadow:0 6px 24px rgba(0,0,0,.08);padding:10px 34px}
.num{font-family:"Outfit",sans-serif;font-weight:600;font-size:66px;line-height:76px;color:var(--numeral);letter-spacing:-2px}
.svc h3,.story h3{font-family:"Outfit",sans-serif;font-weight:500;font-size:21px;letter-spacing:-.6px;margin-top:4px}
.svc p,.story p{font-size:13px;line-height:22px;color:var(--muted);margin-top:6px}
.link-dot{position:absolute;width:40px;height:40px;border-radius:50%;background:var(--pink);display:flex;align-items:center;justify-content:center;box-shadow:0 2px 6px rgba(255,79,151,.35)}
.tagline{position:absolute;top:1128px;left:0;width:1200px;text-align:center;font-family:"Outfit",sans-serif;font-size:16px;letter-spacing:-.5px}

/* about */
.about-text{position:absolute;left:600px;top:1262px;width:436px}
.about-text .eyebrow{font-family:"Outfit",sans-serif;font-size:16px;margin-left:5px;letter-spacing:-.4px}
.about-text h2{font-family:"Outfit",sans-serif;font-weight:500;font-size:38px;line-height:45px;letter-spacing:-1.3px;margin-top:14px}
.about-text p{font-size:13px;line-height:22px;color:var(--muted);margin-top:18px}
.about-text p+p{margin-top:12px}

/* credentials */
.creds{position:absolute;left:0;top:1786px;width:1200px;height:364px;background:var(--pink)}
.cred{position:absolute;top:115px;width:250px;text-align:center;color:var(--white);font-size:17px;line-height:22px}
.cred .ico{width:84px;height:80px;margin:0 auto 12px;background:var(--white);border-radius:8px;display:flex;align-items:center;justify-content:center}
.divider{position:absolute;top:110px;width:1px;height:140px;background:rgba(255,255,255,.45)}

/* help */
.help{position:absolute;left:143px;top:2255px;width:440px}
.help h2{font-family:"Outfit",sans-serif;font-weight:500;font-size:38px;letter-spacing:-1.5px}
.help p{font-size:12.5px;line-height:22px;color:var(--muted);margin-top:10px}
.help ul{list-style:none;margin-top:18px}
.help li{font-size:14px;line-height:35px;display:flex;align-items:center}
.help li::before{content:"";width:10px;height:10px;border-radius:50%;background:var(--pink);margin-right:10px}

/* stories */
.story{position:absolute;top:2811px;width:329px;height:195px;background:var(--card);border-radius:14px;box-shadow:0 6px 24px rgba(0,0,0,.08);padding:6px 24px}

/* testimonials */
.quote-card{position:absolute;left:500px;top:3237px;width:527px;height:258px;background:var(--card);border-radius:0 14px 14px 0;box-shadow:0 6px 24px rgba(0,0,0,.08);padding:26px 52px}
.quote-card p{font-size:15px;line-height:22px;color:var(--muted);margin-top:14px}
.stars{margin-top:6px;display:flex}
.quote-card .name{font-family:"Outfit",sans-serif;font-size:16px;letter-spacing:-.6px;margin-top:6px}
.nav-arrow{position:absolute;top:3332px;width:52px;height:52px;border-radius:50%;display:flex;align-items:center;justify-content:center}

/* faq */
.faq{position:absolute;left:276px;width:647px;height:55px;background:var(--soft);border-radius:8px;display:flex;align-items:center;justify-content:space-between;padding:0 24px 0 28px;font-size:13.5px}
.faq .plus{font-size:24px;font-weight:400;color:var(--ink)}

/* footer */
.footer{position:absolute;left:0;top:4124px;width:1200px;height:381px;background:var(--navy);color:var(--white)}
.footer .brand{position:absolute;left:91px;top:180px;font-size:30px;letter-spacing:3px}
.footer .brand .dot{width:16px;height:16px}
.footer h4{position:absolute;top:60px;font-family:"Outfit",sans-serif;font-weight:500;font-size:29px;letter-spacing:-1.2px}
.contact-row{position:absolute;left:439px;display:flex;gap:12px;font-size:13px;line-height:20px;color:var(--white)}
.contact-row svg{flex:none;margin-top:3px}
.field{position:absolute;height:39px;background:var(--white);border-radius:4px;color:#9a9cab;font-size:12.5px;padding:0 14px;display:flex;align-items:center}
.submit{position:absolute;left:747px;top:212px;width:364px;height:40px;background:var(--pink);border-radius:4px;color:var(--white);font-size:14px;font-weight:500;display:flex;align-items:center;justify-content:center}
.rule{position:absolute;left:89px;top:313px;width:1022px;height:1px;background:rgba(255,255,255,.25)}
.copy{position:absolute;left:0;top:337px;width:1200px;text-align:center;font-size:12.5px;color:var(--white)}
</style>
</head>
<body>

<!-- Hero -->
<section class="hero" role="img" aria-label="Photo of an attorney in a suit working at a laptop in a bright office">
  <div class="shade"></div>
</section>
<header class="topbar">
  <div class="brand"><span class="dot"></span>MAREN HOLBECK</div>
  <nav class="nav"><span>Home</span><span>About</span><span>Services</span><span>Who I Work With</span><span>Testimonials</span><span>Success Stories</span></nav>
  <div class="search"><svg width="16" height="16" viewBox="0 0 16 16" fill="none" stroke="#1f2233" stroke-width="2"><circle cx="7" cy="7" r="5"/><path d="M11 11l4 4"/></svg></div>
  <a class="btn">Contact Us<span class="arrow"><svg width="14" height="14" viewBox="0 0 14 14" fill="none" stroke="#ff4f97" stroke-width="1.6"><path d="M3 11L11 3M5 3h6v6"/></svg></span></a>
</header>
<h1 class="hero-title">Trusted<br>Legal Guidance<br>for Families<small>And Founders</small></h1>
<p class="hero-lead">Whether you’re protecting what you’ve built or building what’s next, I help you navigate estate planning and business law with confidence, compassion, and clarity.</p>
<a class="btn" style="left:89px;top:556px;width:179px;height:51px">Book A Call<span class="arrow"><svg width="14" height="14" viewBox="0 0 14 14" fill="none" stroke="#ff4f97" stroke-width="1.6"><path d="M3 11L11 3M5 3h6v6"/></svg></span></a>
<div class="explore" role="img" aria-label="Circular scroll-down badge"></div>

<!-- What I Help With -->
<h2 class="h2" style="top:832px">What I Help With</h2>
<article class="svc" style="left:217px"><div class="num">01</div><h3>Estate Planning</h3><p>Protect your family, assets, and legacy with thoughtful legal planning tailored to your values.</p></article>
<article class="svc" style="left:609px"><div class="num">02</div><h3>Business Law</h3><p>Set your business up for long-term success with sound legal strategies and proactive guidance.</p></article>
<div class="link-dot" style="left:580px;top:986px"><svg width="16" height="16" viewBox="0 0 16 16" fill="none" stroke="#fff" stroke-width="1.8"><path d="M2 8h12M9 3l5 5-5 5"/></svg></div>
<p class="tagline">Legal Clarity for Life and Business.</p>

<!-- About -->
<div class="photo" style="left:166px;top:1238px;width:388px;height:452px;background:linear-gradient(135deg,#d7dbe0,#9aa3ad 55%,#4a4f5c)" role="img" aria-label="Photo of the attorney meeting a client at a desk"></div>
<div class="about-text">
  <div class="eyebrow">Meet Maren T. Holbeck</div>
  <h2>Attorney, CPA, and Your Trusted Legal Partner</h2>
  <p>I’m Maren, a New York City-based attorney and CPA who helps families and founders feel confident in their legal decisions. With over a decade of experience and more than 500 clients served, I combine financial precision with legal insight — and a deeply human approach.</p>
  <p>I believe legal support should feel clear, compassionate, and empowering. Whether we’re designing your estate plan or helping your business grow, I bring warmth, integrity, and a focus on results.</p>
</div>
<a class="btn" style="left:600px;top:1623px;width:178px;height:51px">Book A Call<span class="arrow"><svg width="14" height="14" viewBox="0 0 14 14" fill="none" stroke="#ff4f97" stroke-width="1.6"><path d="M3 11L11 3M5 3h6v6"/></svg></span></a>

<!-- Credentials -->
<section class="creds">
  <h2 class="h2" style="top:45px;color:#fff">Our Credentials</h2>
  <div class="cred" style="left:100px"><div class="ico"><svg width="50" height="44" viewBox="0 0 50 44" fill="none" stroke="#2f3552" stroke-width="2"><path d="M4 40h42M9 40V26h6v14M20 40V20h6v20M31 40V14h6v26M8 20l10-8 8 5 14-12"/></svg></div>Licensed Attorney<br>New York</div>
  <div class="divider" style="left:353px"></div>
  <div class="cred" style="left:350px"><div class="ico"><svg width="44" height="48" viewBox="0 0 44 48" fill="none" stroke="#2f3552" stroke-width="2"><rect x="6" y="4" width="32" height="40" rx="3"/><rect x="11" y="9" width="22" height="9"/><path d="M12 25h4M20 25h4M28 25h4M12 32h4M20 32h4M28 32h4M12 39h4M20 39h4M28 39h4"/></svg></div>Certified Public<br>Accountant</div>
  <div class="divider" style="left:600px"></div>
  <div class="cred" style="left:600px"><div class="ico"><svg width="48" height="48" viewBox="0 0 48 48" fill="none" stroke="#2f3552" stroke-width="2"><path d="M24 4l16 6v12c0 10-7 18-16 22C15 40 8 32 8 22V10z"/><path d="M16 24l5 5 10-10"/></svg></div>Trusted Advisor to<br>500+ Clients</div>
  <div class="divider" style="left:861px"></div>
  <div class="cred" style="left:850px"><div class="ico"><svg width="48" height="46" viewBox="0 0 48 46" fill="none" stroke="#2f3552" stroke-width="2"><path d="M24 4l6 13 14 1-11 9 4 14-13-8-13 8 4-14L4 18l14-1z"/></svg></div>Perfect 5-Star<br>Ratiang</div>
  <a class="btn light" style="left:511px;top:280px;width:178px;height:49px">Book A Call<span class="arrow"><svg width="14" height="14" viewBox="0 0 14 14" fill="none" stroke="#fff" stroke-width="1.6"><path d="M3 11L11 3M5 3h6v6"/></svg></span></a>
</section>

<!-- How I Can Help -->
<div class="help">
  <h2>How I Can Help</h2>
  <p>It is a long established fact that a reader will be distracted by the readable content of a page when looking at its layout. The point of using Lorem Ipsum is that it has a more...</p>
  <ul>
    <li>Entity Formation (LLC, S-Corp, etc.).</li>
    <li>Contracts &amp; Agreements.</li>
    <li>Flat-Fee Legal Packages.</li>
    <li>Strategic Legal Counsel.</li>
    <li>Risk Mitigation.</li>
  </ul>
</div>
<a class="btn" style="left:143px;top:2580px;width:268px;height:49px">Schedule a Consultation<span class="arrow"><svg width="14" height="14" viewBox="0 0 14 14" fill="none" stroke="#ff4f97" stroke-width="1.6"><path d="M3 11L11 3M5 3h6v6"/></svg></span></a>
<div class="photo" style="left:670px;top:2239px;width:385px;height:420px;background:linear-gradient(160deg,#c9b79d,#8c7a63 45%,#2b2a2e)" role="img" aria-label="Photo of two professionals talking in a hallway"></div>

<!-- Success Stories -->
<h2 class="h2" style="top:2738px">Success Stories</h2>
<article class="story" style="left:89px"><div class="num">01</div><h3>Example 1</h3><p>Helped a young couple secure their children’s future with a full estate plan, including guardianship...</p></article>
<article class="story" style="left:435px"><div class="num">02</div><h3>Example 2</h3><p>Guided a Brooklyn-based creative agency through LLC formation,contracts and long-term legal growth strategy.</p></article>
<article class="story" style="left:782px"><div class="num">03</div><h3>Example 3</h3><p>Reorganized an entrepreneur’s multiple businesses into clear tax efficient structure with legal protection.</p></article>
<div class="link-dot" style="left:407px;top:2892px"><svg width="16" height="16" viewBox="0 0 16 16" fill="none" stroke="#fff" stroke-width="1.8"><path d="M2 8h12M9 3l5 5-5 5"/></svg></div>
<div class="link-dot" style="left:753px;top:2892px"><svg width="16" height="16" viewBox="0 0 16 16" fill="none" stroke="#fff" stroke-width="1.8"><path d="M2 8h12M9 3l5 5-5 5"/></svg></div>
<a class="btn" style="left:519px;top:3035px;width:158px;height:50px">See More<span class="arrow"><svg width="14" height="14" viewBox="0 0 14 14" fill="none" stroke="#ff4f97" stroke-width="1.6"><path d="M3 11L11 3M5 3h6v6"/></svg></span></a>

<!-- Testimonials -->
<h2 class="h2" style="top:3163px">Testimonials</h2>
<div class="nav-arrow" style="left:89px;background:var(--navy)"><svg width="16" height="16" viewBox="0 0 16 16" fill="none" stroke="#fff" stroke-width="1.8"><path d="M14 8H2M7 3L2 8l5 5"/></svg></div>
<div class="abs" style="left:177px;top:3237px;width:323px;height:258px;border-radius:12px 0 0 12px;background:linear-gradient(150deg,#6b6258,#2d2b2c 60%,#171719)" role="img" aria-label="Photo of a team of colleagues reviewing documents at a table"></div>
<div class="quote-card">
  <svg width="64" height="42" viewBox="0 0 64 42" fill="#ff4f97"><path d="M0 42V24C0 10 8 2 20 0l3 6C15 9 12 14 12 20h12v22zM36 42V24C36 10 44 2 56 0l3 6c-8 3-11 8-11 14h12v22z"/></svg>
  <p>We worked with Maren to set up our estate plan documents. She was very knowledgable and helped us to make the best decisions for our family. I particularly appreciated her background.</p>
  <div class="stars">
    <svg width="112" height="20" viewBox="0 0 112 20" fill="#f4a523"><path id="star" d="M10 1l2.6 6 6.4.5-4.9 4.2 1.5 6.3L10 14.6 4.4 18l1.5-6.3L1 7.5 7.4 7z"/><use href="#star" x="22"/><use href="#star" x="44"/><use href="#star" x="66"/><use href="#star" x="88"/></svg>
  </div>
  <div class="name">Dana Whitfield</div>
</div>
<div class="nav-arrow" style="left:1058px;background:var(--pink)"><svg width="16" height="16" viewBox="0 0 16 16" fill="none" stroke="#fff" stroke-width="1.8"><path d="M2 8h12M9 3l5 5-5 5"/></svg></div>

<!-- FAQs -->
<h2 class="h2" style="top:3576px">FAQs</h2>
<div class="faq" style="top:3650px">How can I learn more about Maren Holbeck?<span class="plus">+</span></div>
<div class="faq" style="top:3713px">Isn’t estate planning just for the wealthy?<span class="plus">+</span></div>
<div class="faq" style="top:3776px">What are the initial steps to get started?<span class="plus">+</span></div>
<div class="faq" style="top:3839px">What kind of information do you need from me?<span class="plus">+</span></div>
<div class="faq" style="top:3902px">What if I need to update my estate planning documents?<span class="plus">+</span></div>
<a class="btn" style="left:516px;top:3984px;width:166px;height:51px">View More<span class="arrow"><svg width="14" height="14" viewBox="0 0 14 14" fill="none" stroke="#ff4f97" stroke-width="1.6"><path d="M3 11L11 3M5 3h6v6"/></svg></span></a>

<!-- Footer -->
<footer class="footer">
  <div class="brand"><span class="dot"></span>MAREN HOLBECK</div>
  <h4 style="left:439px">Contact Us</h4>
  <h4 style="left:745px">Request a Quote</h4>
  <div class="contact-row" style="top:110px"><svg width="14" height="14" viewBox="0 0 14 14" fill="#ff4f97"><path d="M3 1l3 3-1.5 2a8 8 0 003.5 3.5L10 8l3 3-2 2C6 13 1 8 1 3z"/></svg><div>Phone:<br>(555) 014-2270</div></div>
  <div class="contact-row" style="top:160px"><svg width="14" height="12" viewBox="0 0 14 12"><path d="M0 1h14v10H0z" fill="#ff4f97"/><path d="M0 1l7 5 7-5" stroke="#2f3552" fill="none"/></svg><div>Email:<br>maren@marenholbecklegal.example</div></div>
  <div class="contact-row" style="top:210px"><svg width="12" height="16" viewBox="0 0 12 16"><path d="M6 0a6 6 0 016 6c0 4-6 10-6 10S0 10 0 6a6 6 0 016-6z" fill="#ff4f97"/><circle cx="6" cy="6" r="2" fill="#2f3552"/></svg><div>Address:<br>48 Linden Row, Fl 9 New York,<br>NY 10001</div></div>
  <div class="field" style="left:747px;top:110px;width:176px">Name*</div>
  <div class="field" style="left:932px;top:110px;width:179px">Email*</div>
  <div class="field" style="left:747px;top:161px;width:176px">Phone*</div>
  <div class="field" style="left:932px;top:161px;width:179px">Address*</div>
  <div class="submit">Submit Now</div>
  <div class="rule"></div>
  <p class="copy">© 2025 Copyright Maren Holbeck All right reserved</p>
  <svg class="abs" style="left:1130px;top:292px" width="46" height="42" viewBox="0 0 46 42" aria-label="Chat"><path d="M23 2c12 0 21 7 21 17s-9 17-21 17c-3 0-6-.5-8-1.5L4 40l3-9C4 28 2 24 2 19 2 9 11 2 23 2z" fill="#ff4f97"/><circle cx="15" cy="19" r="2.5" fill="#fff"/><circle cx="23" cy="19" r="2.5" fill="#fff"/><circle cx="31" cy="19" r="2.5" fill="#fff"/></svg>
</footer>

</body>
</html>
```